Business Card for a Dental Office

The design should communicate integrity, quality and reliability. We also want the card look elegant, simple, but still stand out, different from the traditional-dental-office business card.

Business

```html
<!DOCTYPE html>
<html lang="en">
<head>
<meta charset="utf-8">
<title>Harlow Dental Studio – Business Card</title>
<link rel="stylesheet" href="https://fonts.googleapis.com/css2?family=Didact+Gothic&family=Montserrat:wght@600&display=swap">
<style>
  :root {
    --backdrop: #1e1e1e;
    --card-light: #ececec;
    --card-dark: #0d0d0d;
    --ink: #1a1a1a;
    --gold: #b39b1c;
    --gold-deep: #a18b16;
    --silver: #a9a9a9;
    --muted: #bdbdbd;
  }
  * { margin: 0; padding: 0; box-sizing: border-box; }
  html, body { width: 1200px; height: 1001px; overflow: hidden; background: var(--backdrop); }
  body { position: relative; font-family: "Didact Gothic", sans-serif; color: var(--ink); }

  .card { position: absolute; left: 329px; width: 543px; height: 304px; }
  .card--front { top: 162px; background: linear-gradient(180deg, #f2f2f2, var(--card-light)); }
  .card--back { top: 537px; background: var(--card-dark); }

  .holder { position: absolute; left: 30px; top: 74px; }
  .holder__name { font-family: "Montserrat", sans-serif; font-weight: 600; font-size: 17px; letter-spacing: 0.3px; color: var(--gold); line-height: 1; }
  .holder__role { font-size: 13.5px; margin-top: 4px; }

  .brand { position: absolute; display: flex; align-items: center; gap: 8px; font-family: "Didact Gothic", sans-serif; white-space: nowrap; }
  .brand__mark { width: 22px; height: 22px; background: var(--gold); }
  .brand--front { right: 30px; top: 82px; font-size: 21px; color: var(--ink); }
  .brand--back { left: 0; right: 0; top: 138px; justify-content: center; font-size: 31px; color: var(--silver); gap: 12px; }
  .brand--back .brand__mark { width: 32px; height: 32px; }

  .contact { position: absolute; left: 30px; top: 200px; list-style: none; font-size: 13.5px; line-height: 17px; }
  .contact li { display: flex; align-items: center; gap: 8px; }
  .contact svg { width: 13px; height: 13px; flex: none; }

  .address { position: absolute; right: 30px; top: 200px; font-size: 13.5px; line-height: 17px; text-align: right; font-style: normal; }

  .footer-band { position: absolute; left: 0; bottom: 0; width: 543px; height: 28px; }

  .back__url { position: absolute; left: 0; right: 0; top: 246px; text-align: center; font-size: 13px; letter-spacing: 0.4px; color: var(--muted); }
</style>
</head>
<body>
  <section class="card card--front" aria-label="Business card front">
    <div class="holder">
      <p class="holder__name">JORDAN ELLERY</p>
      <p class="holder__role">General Manager</p>
    </div>

    <div class="brand brand--front"><span class="brand__mark"></span>Harlow Dental Studio</div>

    <ul class="contact">
      <li>
        <svg viewBox="0 0 13 13"><rect width="13" height="13" rx="2" fill="var(--gold)"/><path d="M4 3.2l1.4-.4 1 2-1 .8c.5 1 1.2 1.7 2.2 2.2l.8-1 2 1-.4 1.4c-3 .2-6.2-3-6-6z" fill="#fff"/></svg>
        (555) 014-2290
      </li>
      <li>
        <svg viewBox="0 0 13 13"><rect width="13" height="13" rx="2" fill="var(--gold)"/><rect x="2.5" y="3.5" width="8" height="6" fill="none" stroke="#fff" stroke-width="1"/><path d="M2.5 3.5l4 3.2 4-3.2" fill="none" stroke="#fff" stroke-width="1"/></svg>
        hello@harlowds.com
      </li>
      <li>
        <svg viewBox="0 0 13 13"><rect width="13" height="13" rx="2" fill="var(--gold)"/><circle cx="6.5" cy="6.5" r="4" fill="none" stroke="#fff" stroke-width="0.9"/><path d="M2.5 6.5h8M6.5 2.5c-2 2.2-2 5.8 0 8M6.5 2.5c2 2.2 2 5.8 0 8" fill="none" stroke="#fff" stroke-width="0.8"/></svg>
        www.harlowds.com
      </li>
    </ul>

    <address class="address">
      27 Linden Avenue<br>
      Fairbrook<br>
      GA 30999
    </address>

    <svg class="footer-band" viewBox="0 0 543 28" preserveAspectRatio="none" aria-hidden="true">
      <polygon points="0,2 341,2 333,13 0,13" fill="var(--ink)"/>
      <polygon points="0,18 330,18 326,28 0,28" fill="var(--gold-deep)"/>
      <polygon points="352,0 543,0 543,28 333,28" fill="var(--gold)"/>
    </svg>
  </section>

  <section class="card card--back" aria-label="Business card back">
    <div class="brand brand--back"><span class="brand__mark"></span>Harlow Dental Studio</div>
    <p class="back__url">www.harlowds.com</p>
  </section>
</body>
</html>
```